Travel Agency Website - Simple General

Need a 7 page simple design that is pretty repetitive. Need to be able to load quickly that is SEO optimized. Trying to give ideas on what they can do, be personal as we are local, but at the same time come across as professional and get information easily with little burden.

- Landing Page
- Brambleton Vacations Page
- Family Trips
- Road Trips from Texas
- Other Destinations
- About Us Page
- Contact Us Page

Target Market(s)

Families

Coding

Coded - Design and coding required

Number of Pages Required

5+ page

Colors

Designer to choose colors to be used in the design.

Requirements
Must have
• Like it to flow easily with our logo. Use that for colors, etc.

```html
<!DOCTYPE html>
<html lang="en">
<head>
<meta charset="utf-8">
<title>Wander Far Travel Co. — Plan Your Perfect Trip</title>
<link rel="stylesheet" href="https://fonts.googleapis.com/css2?family=Cormorant+Garamond:wght@500&family=Jost:wght@400;500&family=Nunito:wght@800&family=Figtree:wght@400;500&display=swap">
<style>
:root{
  --teal-dark:#1b5866;
  --teal:#23807e;
  --teal-text:#1f5f6b;
  --gold:#c49a4d;
  --gold-light:#d6b26a;
  --white:#ffffff;
  --ink:#2c3a3f;
}
*{box-sizing:border-box;margin:0;padding:0}
html,body{width:1200px;height:946px;overflow:hidden}
body{
  position:relative;
  background:linear-gradient(180deg,#f7f4ee 0%,#ece9e2 38%,#f1eee7 70%,#f3f1ec 100%);
  font-family:"Figtree",sans-serif;color:var(--teal-text);
}
h1,h2{font-weight:400}
a{text-decoration:none}
.topbar{position:absolute;left:0;top:0;width:1200px;height:43px;background:var(--teal-dark);color:var(--white);font-size:14px}
.topbar .contact{position:absolute;top:9px;display:flex;align-items:center;gap:9px}
.topbar .contact.email{left:583px}
.topbar .contact.phone{left:874px;font-size:15.5px}
.topbar .icon{width:26px;height:26px;border-radius:50%;background:var(--white);display:flex;align-items:center;justify-content:center}
.brand{position:absolute;left:92px;top:58px;width:180px;display:flex;align-items:center;gap:10px;font-weight:500;font-size:22px;line-height:1.1;color:var(--teal-dark)}
.brand .dot{width:26px;height:26px;border-radius:50%;background:var(--gold);flex:none}
.nav{position:absolute;left:298px;top:85px;display:flex;align-items:center;font-size:15px}
.nav a{color:var(--teal-text);margin-right:18px;white-space:nowrap}
.nav a.about{margin-left:10px;margin-right:0}
.nav .home{display:flex}
.btn-contact{position:absolute;left:981px;top:75px;width:144px;height:38px;border-radius:19px;background:var(--gold);color:var(--white);font-size:14.5px;display:flex;align-items:center;padding-left:27px}
.btn-contact .arrow{position:absolute;right:7px;top:7px;width:24px;height:24px;border-radius:50%;background:var(--gold-light);display:flex;align-items:center;justify-content:center}
.kicker{position:absolute;left:0;width:1210px;top:174px;text-align:center;font-family:"Jost",sans-serif;font-weight:400;font-size:31px;letter-spacing:1px;color:var(--teal-text)}
.headline{position:absolute;left:0;width:1210px;top:222px;justify-content:center;font-family:"Cormorant Garamond",serif;font-weight:500;font-size:62px;letter-spacing:1px;color:var(--teal-text);display:flex;align-items:center;white-space:nowrap}
.headline .mark{background:var(--teal);color:var(--white);border-radius:4px;padding:2px 16px 0 19px;margin:0 13px;height:75px;display:flex;align-items:center}
.card{position:absolute;border-radius:6px;overflow:hidden}
.card .photo{position:absolute;inset:0}
.card .shade{position:absolute;left:0;right:0;bottom:0;height:45%;background:linear-gradient(180deg,rgba(27,88,102,0) 0%,rgba(27,88,102,.75) 100%)}
.card .label{position:absolute;left:29px;bottom:22px;font-family:"Nunito",sans-serif;font-weight:800;font-size:22px;letter-spacing:.3px;color:var(--white);line-height:1.1;white-space:nowrap}
.card .label small{display:block;font-size:11.5px;letter-spacing:0;margin-top:4px}
.card .go{position:absolute;right:12px;bottom:17px;width:34px;height:34px;border-radius:50%;background:var(--white);display:flex;align-items:center;justify-content:center}
.card-brambleton{left:92px;top:351px;width:338px;height:469px}
.card-brambleton .photo{background:linear-gradient(180deg,#0d55b4 0%,#2a7fd0 40%,#c9c2b8 62%,#8a9aa6 100%)}
.card-brambleton .label{left:26px;font-size:19px;letter-spacing:0;bottom:24px}
.card-family{left:442px;top:351px;width:339px;height:227px}
.card-family .photo{background:linear-gradient(180deg,#a9cde6 0%,#8fb6cc 40%,#5d8ea3 70%,#d8dfe2 100%)}
.card-road{left:443px;top:591px;width:339px;height:227px}
.card-road .photo{background:linear-gradient(180deg,#e9a07a 0%,#f0b870 30%,#3f5a2c 55%,#4b4a58 100%)}
.card-road .label{bottom:16px}
.card-other{left:794px;top:351px;width:338px;height:469px}
.card-other .photo{background:linear-gradient(160deg,#8b2a14 0%,#c8621c 35%,#e7b47c 60%,#c96b24 85%,#8d4318 100%)}
.card-other .label{left:32px}
.footer{position:absolute;left:0;top:880px;width:1200px;height:66px;background:var(--white)}
.footer p{position:absolute;left:0;width:1210px;top:24px;text-align:center;font-family:"Jost",sans-serif;font-size:14px;letter-spacing:.4px;color:var(--ink)}
.footer .social{position:absolute;left:1032px;top:19px;display:flex;gap:8px}
.footer .social span{width:24px;height:24px;border-radius:50%;background:var(--teal-dark)}
</style>
</head>
<body>
<header class="topbar">
  <div class="contact email">
    <span class="icon"><svg width="14" height="10" viewBox="0 0 14 10"><rect x=".7" y=".7" width="12.6" height="8.6" rx="1" fill="none" stroke="#1b5866" stroke-width="1.4"/><path d="M1 1l6 5 6-5" fill="none" stroke="#1b5866" stroke-width="1.4"/></svg></span>
    hello@wanderfartravel.com
  </div>
  <div class="contact phone">
    <span class="icon"><svg width="13" height="13" viewBox="0 0 24 24"><path fill="#1b5866" d="M6.6 10.8a15.1 15.1 0 006.6 6.6l2.2-2.2c.3-.3.7-.4 1-.2 1.1.4 2.3.6 3.6.6.6 0 1 .4 1 1V20c0 .6-.4 1-1 1A17 17 0 013 4c0-.6.4-1 1-1h3.5c.6 0 1 .4 1 1 0 1.3.2 2.5.6 3.6.1.3 0 .7-.2 1z"/></svg></span>
    Phone Number (123) 555 0182
  </div>
</header>

<div class="brand"><span class="dot"></span>Wander Far<br>Travel Co.</div>

<nav class="nav">
  <a class="home" href="#"><svg width="14" height="13" viewBox="0 0 14 13"><path d="M7 0l7 6h-2v7H9V9H5v4H2V6H0z" fill="#c49a4d"/></svg></a>
  <a href="#">Brambleton Vacations</a>
  <a href="#">Family Trips</a>
  <a href="#">Texas Road Trips</a>
  <a href="#">Other Destinations</a>
  <a class="about" href="#">About Us</a>
</nav>
<a class="btn-contact" href="#">Contact Us<span class="arrow"><svg width="10" height="10" viewBox="0 0 10 10"><path d="M2 8l6-6M3 2h5v5" fill="none" stroke="#fff" stroke-width="1.5"/></svg></span></a>

<h2 class="kicker">WANDER FAR TRAVEL CO.</h2>
<h1 class="headline">PLAN YOUR <span class="mark">PERFECT</span> TRIP</h1>

<a class="card card-brambleton" href="#">
  <div class="photo" role="img" aria-label="Fairytale castle with blue spires under a clear sky"></div>
  <div class="shade"></div>
  <span class="label">BRAMBLETON VACATIONS</span>
  <span class="go"><svg width="12" height="12" viewBox="0 0 10 10"><path d="M2 8l6-6M3 2h5v5" fill="none" stroke="#1b5866" stroke-width="1.6"/></svg></span>
</a>
<a class="card card-family" href="#">
  <div class="photo" role="img" aria-label="Family enjoying a sailboat ride on open water"></div>
  <div class="shade"></div>
  <span class="label">FAMILY TRIPS</span>
  <span class="go"><svg width="12" height="12" viewBox="0 0 10 10"><path d="M2 8l6-6M3 2h5v5" fill="none" stroke="#1b5866" stroke-width="1.6"/></svg></span>
</a>
<a class="card card-road" href="#">
  <div class="photo" role="img" aria-label="Open country road at sunset with a water tower and trees"></div>
  <div class="shade"></div>
  <span class="label">TEXAS ROAD TRIPS<small>(Partnership with Piney Lane Van Rentals</small></span>
  <span class="go"><svg width="12" height="12" viewBox="0 0 10 10"><path d="M2 8l6-6M3 2h5v5" fill="none" stroke="#1b5866" stroke-width="1.6"/></svg></span>
</a>
<a class="card card-other" href="#">
  <div class="photo" role="img" aria-label="Hikers beneath a red rock arch in a desert landscape"></div>
  <div class="shade"></div>
  <span class="label">OTHER DESTINATIONS</span>
  <span class="go"><svg width="12" height="12" viewBox="0 0 10 10"><path d="M2 8l6-6M3 2h5v5" fill="none" stroke="#1b5866" stroke-width="1.6"/></svg></span>
</a>

<footer class="footer">
  <p>© 2026 Wander Far Travel Co. All Right Reserved</p>
  <div class="social"><span aria-label="Social profile"></span><span aria-label="Social profile"></span></div>
</footer>
</body>
</html>
```